Ardenwell Building and Property Services needs a business card design

We need a business card design for our building and property services business. We already have a logo we just need a creative design and layout on a business card. Emphasis on clean, modern, professional.
Our client targets are mainly body corporates, building managers, construction managers.
We are a building services company that lean more to structural repair of buildings, through concrete rectification and carbon fibre strengthening.
We also refurbish facades, rendering, painting etc
We target higher end body corporates in prestigious locations, hence why we'd like our cards to reflect professionalism, strength, efficiency

Target Market(s)

body corporates, building managers, construction managers

Industry/Entity Type

Construction

Contact Information for Business Card

Ardenwell is the main word, with 'Building and Property Services' underneath.
Level 17, 82 Harlow Street
MERRIDALE
Melbourne
Vic 3094
T: 9518 2736
Duncan Ferris - Director
dunardenwell@mailbox-example.com

Requirements
Must have
• Stand out on the back of the card- strong/ bold, company logo
• All of the contact details written above
Should not have
• I'd like the card to stand out, especially on the back. Id like the company logo to be prominent, although feel free to be creative around it. But remain clean and professional

```html
<!DOCTYPE html>
<html lang="en">
<head>
<meta charset="utf-8">
<title>Ardenwell Building and Property Services – Business Card</title>
<link rel="stylesheet" href="https://fonts.googleapis.com/css2?family=Arimo:wght@400;700&display=swap">
<style>
  :root {
    --page: #e9e9ec;
    --back-black: #050507;
    --back-glow: #1d4a66;
    --navy: #17175e;
    --navy-deep: #0d0d44;
    --navy-mid: #1f1f6c;
    --cyan: #38c4f3;
    --ink: #0f1040;
    --shadow: rgba(10, 10, 40, 0.35);
  }
  * { box-sizing: border-box; margin: 0; padding: 0; }
  html, body {
    width: 1200px; height: 800px; overflow: hidden;
    background: var(--page);
    font-family: "Arimo", Arial, sans-serif;
  }
  .canvas { position: relative; width: 1200px; height: 800px; }

  .card {
    position: absolute;
    width: 560px; height: 320px;
    border-radius: 4px;
    overflow: hidden;
    box-shadow: 0 14px 30px var(--shadow);
  }

  /* Back of card */
  .card-back { left: 30px; top: 70px; background: var(--back-black); }
  .back-texture {
    position: absolute; inset: 0;
    background: radial-gradient(ellipse at 50% 50%, var(--back-glow) 0%, #0b1a26 35%, var(--back-black) 75%);
  }
  .back-brand {
    position: absolute; left: 0; right: 0; top: 50%;
    transform: translateY(-50%);
    display: flex; align-items: center; justify-content: center; gap: 16px;
  }
  .back-brand .mark-square { width: 34px; height: 34px; background: var(--cyan); }
  .back-brand .brand-name {
    font-size: 48px; font-weight: 700; color: var(--cyan); letter-spacing: 2px;
  }

  /* Front of card */
  .card-front { left: 610px; top: 410px; background: var(--navy); }
  .front-shapes { position: absolute; inset: 0; }
  .front-brand {
    position: absolute; left: 30px; width: 280px; top: 118px;
    text-align: center; color: var(--cyan);
  }
  .front-brand .mark-square {
    display: block; width: 40px; height: 40px; margin: 0 auto 18px;
    background: var(--cyan);
  }
  .front-brand .brand-name {
    font-size: 40px; font-weight: 700; letter-spacing: 3px; text-transform: uppercase;
  }
  .front-brand .brand-line {
    margin-top: 4px; font-size: 10.5px; font-weight: 700; letter-spacing: 1.6px; text-transform: uppercase;
  }

  .name-band {
    position: absolute; left: 348px; right: 0; top: 44px; height: 56px;
    background: var(--cyan); color: var(--ink);
    padding: 8px 0 0 40px;
  }
  .name-band .person { font-size: 24px; font-weight: 700; line-height: 1; }
  .name-band .role { font-size: 15px; font-weight: 700; letter-spacing: 1.5px; margin-top: 3px; }

  .contacts {
    position: absolute; left: 330px; right: 10px; top: 110px;
    text-align: center; color: var(--cyan); font-weight: 700;
  }
  .contact { display: flex; flex-direction: column; align-items: center; margin-bottom: 6px; }
  .contact svg { display: block; margin-bottom: 3px; }
  .contact .phone { font-size: 19px; letter-spacing: 1px; line-height: 1.15; }
  .contact .email { font-size: 12px; line-height: 1.2; }
  .contact .address { font-size: 13px; line-height: 1.3; }
</style>
</head>
<body>
<main class="canvas">

  <section class="card card-back" aria-label="Back of business card">
    <div class="back-texture" role="img" aria-label="Dark mesh texture with a soft blue glow behind the brand"></div>
    <div class="back-brand">
      <span class="mark-square" aria-hidden="true"></span>
      <span class="brand-name">Ardenwell</span>
    </div>
  </section>

  <section class="card card-front" aria-label="Front of business card">
    <svg class="front-shapes" width="560" height="320" viewBox="0 0 560 320" aria-hidden="true">
      <rect width="560" height="320" fill="var(--navy)"/>
      <path d="M0 0 H300 C360 90 370 230 330 320 H0 Z" fill="var(--navy-deep)"/>
      <path d="M300 0 C360 90 370 230 330 320 H345 C385 230 375 90 318 0 Z" fill="var(--navy-mid)"/>
    </svg>

    <div class="front-brand">
      <span class="mark-square" aria-hidden="true"></span>
      <div class="brand-name">Ardenwell</div>
      <div class="brand-line">Building and Property Services</div>
    </div>

    <div class="name-band">
      <div class="person">Duncan Ferris</div>
      <div class="role">Director</div>
    </div>

    <div class="contacts">
      <div class="contact">
        <svg width="26" height="18" viewBox="0 0 26 18" aria-hidden="true">
          <path d="M2 9 C2 2 24 2 24 9 L19 10 L18 6 C15 5 11 5 8 6 L7 10 Z" fill="var(--cyan)"/>
          <rect x="7" y="11" width="12" height="6" rx="1.5" fill="var(--cyan)"/>
        </svg>
        <span class="phone">9518 2736</span>
      </div>
      <div class="contact">
        <svg width="26" height="17" viewBox="0 0 26 17" aria-hidden="true">
          <rect x="1" y="1" width="24" height="15" fill="none" stroke="var(--cyan)" stroke-width="2"/>
          <path d="M1 1 L13 10 L25 1" fill="none" stroke="var(--cyan)" stroke-width="2"/>
        </svg>
        <span class="email">dunardenwell@mailbox-example.com</span>
      </div>
      <div class="contact">
        <svg width="16" height="22" viewBox="0 0 16 22" aria-hidden="true">
          <path d="M8 21 C3 14 1 11 1 8 A7 7 0 0 1 15 8 C15 11 13 14 8 21 Z" fill="var(--cyan)"/>
          <circle cx="8" cy="8" r="3" fill="var(--navy)"/>
        </svg>
        <span class="address">Level 17, 82 Harlow Street<br>MERRIDALE<br>Melbourne<br>Vic 3094</span>
      </div>
    </div>
  </section>

</main>
</body>
</html>
```